Roadside building business signage for a holistic health clinic.

Replace signs as shown in the attached file. They are perforated stickers that go on the windows as shown. Looking for something that has our logo and says the name of the practice with logo (Fernbrook Health & Wellness) also boldly says Acupuncture, IV Vitamins, and Holistic Health.
Possibly our phone number as well 318-627-5194
Updates

Please don't use pink except the logo. Earthy, organic tone colors appreciated.

Need of eye catching window signage of a holistic clinic on a brick building. Pink, purple, sage green, white color. Logo is pink on a white background. Please don't overload with too much pink. Words to include are "Fernbrook Health and Wellness(name of business)", "Direct Primary Care", " Medical acupuncture", "IV Vitamin Therapy", "fernbrookcare-example.com","318-627-5194".

Target Market(s)

People will see in their cars passing by the building. Busy roadside so need to be visible while passing in fast speed.

Industry/Entity Type

Health & Wellness

Font styles to use
Sans Serif

Colors

Designer to choose colors to be used in the design.

Requirements
Must have
• On sign must have words Holistic Medicine, Medical Acupuncture, Direct Primary Care and IV vitamins.
Nice to have
• Simple, minimalistic, artistic yet has clear message. White, Black, Violet, Pink (logo), Dark green, Sage green.
Should not have
• Bold colors (red, yellow, blue), same tone colors. Blue waves on the current signage (uploaded file) must go.

```html
<!DOCTYPE html>
<html lang="en">
<head>
<meta charset="utf-8">
<title>Fernbrook Health &amp; Wellness – Window Signage</title>
<link rel="stylesheet" href="https://fonts.googleapis.com/css2?family=Kurale&family=Itim&display=swap">
<style>
  :root {
    --canvas: #ffffff;
    --panel: #ffffff;
    --panel-shadow: rgba(0, 0, 0, 0.08);
    --leaf-green: #7cc242;
    --sky-blue: #1ba0d8;
    --forest: #1f4b3a;
    --wash-yellow: #fbe7a6;
    --wash-cream: #fdf3d2;
    --wash-sage: #cfe6b8;
    --wash-mint: #cfe9dc;
    --wash-blue: #8fd0ec;
    --wash-lilac: #b9c4ef;
    --palm-tan: #d9c79a;
    --cell: 149px;
    --step: 157px;
  }
  * { box-sizing: border-box; margin: 0; padding: 0; }
  html, body { width: 1200px; height: 540px; overflow: hidden; background: var(--canvas); }
  .signage { position: relative; width: 1200px; height: 540px; }
  .window-set { position: absolute; left: 211px; top: 38px; width: 777px; height: 463px; }
  .pane {
    position: absolute; width: var(--cell); height: var(--cell);
    background: var(--panel); overflow: hidden;
    box-shadow: 0 0 3px var(--panel-shadow);
  }
  .arch-left { border-top-left-radius: 149px; }
  .arch-right { border-top-right-radius: 149px; }

  .wash { position: absolute; inset: 0; }
  .deco { position: absolute; }

  .brand {
    position: absolute; left: 0; right: 0; top: 66px;
    text-align: center; color: var(--forest);
    font-family: "Kurale", serif; font-weight: 400;
  }
  .brand-dot {
    display: block; width: 22px; height: 22px; margin: 0 auto 8px;
    border-radius: 50%; background: var(--forest);
  }
  .brand-name { display: block; font-size: 19px; letter-spacing: 3px; line-height: 1; }
  .brand-sub { display: block; font-size: 6px; letter-spacing: 2px; margin-top: 3px; }

  .headline {
    position: absolute; left: 12px; top: 22px;
    font-family: "Kurale", serif; font-size: 19.5px; line-height: 26px;
    color: var(--leaf-green);
  }
  .phone { position: absolute; font-family: "Kurale", serif; font-size: 19px; }
  .phone-green { color: var(--leaf-green); right: 10px; bottom: 10px; }
  .phone-blue { color: var(--sky-blue); left: 10px; top: 12px; }

  .services {
    position: absolute; left: 8px; top: 12px; list-style: none;
    font-family: "Itim", sans-serif; font-size: 16.5px; line-height: 17px;
    color: var(--sky-blue);
  }
  .services li { position: relative; padding-left: 14px; margin-bottom: 9px; }
  .services li::before {
    content: ""; position: absolute; left: 1px; top: 5px;
    width: 7px; height: 7px; border-radius: 50%; background: var(--sky-blue);
  }
</style>
</head>
<body>
<main class="signage">
  <section class="window-set" aria-label="Fernbrook Health &amp; Wellness window signage layout">

    <!-- Arch row -->
    <div class="pane arch-left" style="left:314px; top:0;">
      <div class="wash" role="img" aria-label="Soft sage and cream watercolour wash" style="background:linear-gradient(180deg, #fff 0%, #fff 55%, var(--wash-sage) 100%), radial-gradient(circle at 90% 20%, var(--wash-cream), transparent 60%);"></div>
      <div class="brand">
        <span class="brand-dot"></span>
        <span class="brand-name">FERNBROOK</span>
        <span class="brand-sub">HEALTH &amp; WELLNESS</span>
      </div>
    </div>
    <div class="pane arch-right" style="left:471px; top:0;">
      <div class="wash" role="img" aria-label="Warm yellow watercolour wash" style="background:radial-gradient(circle at 40% 100%, var(--wash-yellow), var(--wash-cream) 60%, #fff 100%);"></div>
      <div class="brand">
        <span class="brand-dot"></span>
        <span class="brand-name">FERNBROOK</span>
        <span class="brand-sub">HEALTH &amp; WELLNESS</span>
      </div>
    </div>

    <!-- Middle row -->
    <div class="pane" style="left:157px; top:158px;">
      <div class="wash" role="img" aria-label="Mint and sage watercolour brush stroke" style="background:linear-gradient(180deg, var(--wash-mint) 0%, var(--wash-sage) 40%, #fff 70%);"></div>
    </div>
    <div class="pane" style="left:314px; top:158px;">
      <div class="wash" style="background:linear-gradient(160deg, var(--wash-sage) 0%, #fff 25%);"></div>
      <p class="headline">Acupuncture,<br>IV Vitamins,<br>and Holistic<br>Health</p>
    </div>
    <div class="pane" style="left:471px; top:158px;">
      <div class="wash" role="img" aria-label="Large faint yellow flower outline decoration" style="background:radial-gradient(circle at 85% 75%, var(--wash-yellow) 0%, var(--wash-cream) 45%, #fff 80%);"></div>
    </div>
    <div class="pane" style="left:628px; top:158px;">
      <div class="wash" role="img" aria-label="Large faint yellow flower outline decoration" style="background:radial-gradient(circle at 10% 60%, var(--wash-yellow) 0%, var(--wash-cream) 55%, #fff 95%);"></div>
      <span class="phone phone-green">318-627-5194</span>
    </div>

    <!-- Bottom row -->
    <div class="pane" style="left:0; top:314px;">
      <div class="wash" role="img" aria-label="Blue and lilac watercolour wash with line-drawn lily" style="background:linear-gradient(120deg, var(--wash-lilac) 0%, var(--wash-blue) 45%, var(--wash-mint) 100%);"></div>
    </div>
    <div class="pane" style="left:157px; top:314px;">
      <div class="wash" role="img" aria-label="Mint watercolour wash with line-drawn lily" style="background:linear-gradient(180deg, #fff 20%, var(--wash-mint) 70%, var(--wash-sage) 100%);"></div>
      <span class="phone phone-blue">318-627-5194</span>
    </div>
    <div class="pane" style="left:314px; top:314px;">
      <div class="deco" role="img" aria-label="Green and yellow leaf sprig illustration" style="left:10px; top:25px; width:139px; height:124px; background:radial-gradient(ellipse at 60% 70%, #dbe99a 0%, #eef5c9 50%, transparent 75%);"></div>
    </div>
    <div class="pane" style="left:471px; top:314px;">
      <ul class="services">
        <li>Holistic<br>Medicine</li>
        <li>Medical<br>Acupuncture</li>
        <li>Direct Primary<br>Care</li>
      </ul>
    </div>
    <div class="pane" style="left:628px; top:314px;">
      <div class="deco" role="img" aria-label="Tan palm frond illustration" style="left:40px; top:0; width:109px; height:149px; background:radial-gradient(ellipse at 80% 50%, var(--palm-tan) 0%, #efe6cc 45%, transparent 75%);"></div>
    </div>

  </section>
</main>
</body>
</html>
```